Harbor Dental, LLC business card project

Business card to be designed with current logo.
Dental office- please keep design of card that looks clean and professional.
Please include the following info:
Harbor Dental, LLC
Dr. Corinne Pelham
3187 Elmwood
Millbrook, PA 18042
610-392-7158
harbordental.office@quillmail.net
Updates
Hello everyone-
Project Deadline Extended
Reason: Just got back from overseas- will look at all designs and provide feedback. Thank you!
Project Deadline Extended
Reason: Polling my friends for the final selection-
thank you to all those that participated- so many talented designers!
Business

```html
<!DOCTYPE html>
<html lang="en">
<head>
<meta charset="utf-8">
<title>Harbor Dental, LLC — Business Card</title>
<link rel="stylesheet" href="https://fonts.googleapis.com/css2?family=Arimo:wght@400;700&display=swap">
<style>
  :root {
    --lime: #b3d236;
    --leaf: #659e3d;
    --text-green: #76ae47;
    --name-green: #689f3f;
    --paper: #ffffff;
  }
  * { margin: 0; padding: 0; box-sizing: border-box; }
  html, body {
    width: 1200px;
    height: 686px;
    overflow: hidden;
    background: var(--paper);
  }
  .card {
    position: relative;
    width: 1200px;
    height: 686px;
    background: var(--paper);
    font-family: "Arimo", Arial, sans-serif;
    overflow: hidden;
  }
  .accents {
    position: absolute;
    inset: 0;
    width: 1200px;
    height: 686px;
  }
  .accent-top { fill: none; stroke: var(--lime); stroke-width: 10; stroke-linecap: round; }
  .accent-bottom { fill: none; stroke: var(--leaf); stroke-width: 10; stroke-linecap: round; }

  .brand {
    position: absolute;
    left: 44px;
    top: 158px;
    display: flex;
    align-items: center;
    gap: 30px;
  }
  .brand-dot {
    width: 96px;
    height: 96px;
    border-radius: 50%;
    background: var(--lime);
    flex: none;
  }
  .brand-name {
    font-size: 110px;
    font-weight: 400;
    color: var(--leaf);
    letter-spacing: -1px;
    line-height: 1;
    white-space: nowrap;
  }

  .contact {
    position: absolute;
    left: 0;
    right: 0;
    top: 348px;
    text-align: center;
    color: var(--text-green);
  }
  .dentist {
    font-size: 34px;
    font-weight: 700;
    color: var(--name-green);
    line-height: 44px;
    margin-bottom: 16px;
  }
  .address, .reach {
    font-size: 32px;
    font-weight: 400;
    letter-spacing: 2px;
    line-height: 44px;
    white-space: nowrap;
  }
  .divider { margin: 0 10px; }
</style>
</head>
<body>
  <div class="card">
    <svg class="accents" viewBox="0 0 1200 686" aria-hidden="true">
      <path class="accent-top" d="M760 110 Q 960 50 1180 40"/>
      <path class="accent-bottom" d="M20 640 Q 240 630 440 575"/>
    </svg>

    <div class="brand">
      <span class="brand-dot" aria-hidden="true"></span>
      <span class="brand-name">Harbor Dental, LLC</span>
    </div>

    <div class="contact">
      <p class="dentist">Dr. Corinne Pelham</p>
      <p class="address">3187 Elmwood, Millbrook, PA 18042</p>
      <p class="reach">ph: 610-392-7158<span class="divider">|</span>e-mail: harbordental.office@quillmail.net</p>
    </div>
  </div>
</body>
</html>
```